依頼概要
初めまして。よろしくお願いいたします。

依頼内容
※エコー(赤ちゃん)ポスターのデザイン依頼

※エコー写真をスキャンして嵌め込みますので、そちらを想定したテンプレート型のポスターデザインをお願いいたします。

※エコーの枚数は3・6・9枚の何れかでお願いいたします。

※子供の名前 身長体重 出産時間 等

ポスターデザインのイメージや雰囲気は
デザイナー様各々におまかせしております。

```html
<!DOCTYPE html>
<html lang="ja">
<head>
<meta charset="utf-8">
<title>Welcome to the World Poster</title>
<link rel="stylesheet" href="https://fonts.googleapis.com/css2?family=Amatic+SC:wght@400;700&family=Cinzel:wght@400;700&display=swap">
<style>
  :root {
    --paper: #ffffff;
    --gold: #c29a5c;
    --gold-deep: #a27a3e;
    --gold-light: #e6cf9c;
    --gold-pale: #f3e6c8;
    --ring-edge: #8a6a35;
    --echo-dark: #1c1c1c;
    --echo-mid: #6d6a66;
    --echo-light: #b9b5ae;
    --ink-light: #ffffff;
  }
  * { margin: 0; padding: 0; box-sizing: border-box; }
  html, body { width: 849px; height: 1200px; overflow: hidden; background: var(--paper); }
  .poster {
    position: relative;
    width: 849px;
    height: 1200px;
    background: var(--paper);
    overflow: hidden;
  }
  .sparkle-field {
    position: absolute;
    left: 0;
    width: 849px;
  }
  .sparkle-field--top {
    top: 0;
    height: 300px;
    background:
      radial-gradient(ellipse at 15% 10%, rgba(194,154,92,0.35), transparent 45%),
      radial-gradient(ellipse at 85% 8%, rgba(194,154,92,0.35), transparent 45%),
      radial-gradient(ellipse at 50% 0%, rgba(230,207,156,0.4), transparent 60%);
  }
  .sparkle-field--bottom {
    top: 760px;
    height: 200px;
    background:
      radial-gradient(ellipse at 10% 90%, rgba(194,154,92,0.35), transparent 55%),
      radial-gradient(ellipse at 90% 80%, rgba(194,154,92,0.35), transparent 55%);
  }
  .welcome-banner {
    position: absolute;
    left: 62px;
    top: 28px;
    width: 725px;
    height: 65px;
    background: linear-gradient(180deg, var(--gold-light), var(--gold) 55%, var(--gold-deep));
    display: flex;
    align-items: center;
    justify-content: center;
  }
  .welcome-banner__text {
    font-family: "Cinzel", serif;
    font-weight: 400;
    font-size: 34px;
    letter-spacing: 3px;
    color: var(--gold-pale);
    -webkit-text-stroke: 0.6px var(--gold-deep);
  }
  .echo-grid {
    position: absolute;
    left: 0;
    top: 0;
  }
  .echo-frame {
    position: absolute;
    width: 238px;
    height: 238px;
    border-radius: 50%;
    background: linear-gradient(145deg, var(--gold-pale), var(--gold) 45%, var(--gold-deep));
    box-shadow: 0 2px 4px rgba(0,0,0,0.25);
    padding: 7px;
  }
  .echo-frame__photo {
    width: 100%;
    height: 100%;
    border-radius: 50%;
    border: 2px solid var(--ring-edge);
    background: radial-gradient(ellipse at 50% 55%, var(--echo-light) 0%, var(--echo-mid) 35%, var(--echo-dark) 72%);
  }
  .birth-band {
    position: absolute;
    left: 0;
    top: 880px;
    width: 849px;
    height: 320px;
  }
  .baby-name {
    position: absolute;
    left: 26px;
    top: 935px;
    font-family: "Amatic SC", sans-serif;
    font-weight: 400;
    font-size: 250px;
    line-height: 1;
    color: var(--ink-light);
    letter-spacing: 6px;
  }
  .birth-details {
    position: absolute;
    left: 548px;
    top: 958px;
    width: 272px;
    height: 205px;
    border: 2px solid var(--ink-light);
    padding: 14px 18px;
    font-family: "Amatic SC", sans-serif;
    font-weight: 700;
    font-size: 44px;
    line-height: 1.2;
    color: var(--ink-light);
    letter-spacing: 3px;
  }
</style>
</head>
<body>
<main class="poster">
  <div class="sparkle-field sparkle-field--top" role="img" aria-label="Scattered gold confetti dots"></div>
  <div class="sparkle-field sparkle-field--bottom" role="img" aria-label="Scattered gold confetti dots"></div>

  <header class="welcome-banner">
    <span class="welcome-banner__text">WELCOM TO THE WORLD!!</span>
  </header>

  <section class="echo-grid" aria-label="Ultrasound photos">
    <div class="echo-frame" style="left:51px;top:158px"><div class="echo-frame__photo" role="img" aria-label="Ultrasound scan photo 1"></div></div>
    <div class="echo-frame" style="left:306px;top:158px"><div class="echo-frame__photo" role="img" aria-label="Ultrasound scan photo 2"></div></div>
    <div class="echo-frame" style="left:561px;top:158px"><div class="echo-frame__photo" role="img" aria-label="Ultrasound scan photo 3"></div></div>
    <div class="echo-frame" style="left:51px;top:396px"><div class="echo-frame__photo" role="img" aria-label="Ultrasound scan photo 4"></div></div>
    <div class="echo-frame" style="left:306px;top:396px"><div class="echo-frame__photo" role="img" aria-label="Ultrasound scan photo 5"></div></div>
    <div class="echo-frame" style="left:561px;top:396px"><div class="echo-frame__photo" role="img" aria-label="Ultrasound scan photo 6"></div></div>
    <div class="echo-frame" style="left:51px;top:639px"><div class="echo-frame__photo" role="img" aria-label="Ultrasound scan photo 7"></div></div>
    <div class="echo-frame" style="left:306px;top:639px"><div class="echo-frame__photo" role="img" aria-label="Ultrasound scan photo 8"></div></div>
    <div class="echo-frame" style="left:561px;top:639px"><div class="echo-frame__photo" role="img" aria-label="Ultrasound scan photo 9"></div></div>
  </section>

  <svg class="birth-band" viewBox="0 0 849 320" aria-hidden="true">
    <defs>
      <linearGradient id="bandGold" x1="0" y1="0" x2="0" y2="1">
        <stop offset="0" stop-color="#c9a468"/>
        <stop offset="1" stop-color="#b88f52"/>
      </linearGradient>
    </defs>
    <path d="M0 40 C 180 5, 330 0, 450 20 S 700 45, 849 10 L 849 320 L 0 320 Z" fill="url(#bandGold)"/>
  </svg>

  <h1 class="baby-name">NAMAE</h1>
  <div class="birth-details">
    <p>48cm 3090g</p>
    <p>2020.03.20</p>
    <p>AM7:36 birth!</p>
  </div>
</main>
</body>
</html>
```